Varnok Develoipment and Management Corp Web Design Project

Website... Based on logo. Update forthcoming....
Updates

Reason: Extended to include recently completed logo design.

Target Market(s)

Financiers, investors, public officials, and landowners.

Industry/Entity Type

Management

Requirements
Should not have
• No palm trees, mayan ruins, or other Caribbean references.

```html
<!DOCTYPE html>
<html lang="en">
<head>
<meta charset="utf-8">
<title>Varnok Development and Management Corp</title>
<link href="https://fonts.googleapis.com/css2?family=Raleway:wght@300;400;600;700&family=Roboto:wght@300;400&family=Open+Sans:wght@400;600&family=Lora:ital@1&display=swap" rel="stylesheet">
<style>
:root{
  --green:#a4bf3a;
  --blue:#2a8fc6;
  --link:#2a8fc6;
  --ink:#3a3a3a;
  --muted:#6f6f6f;
  --soft:#f5f5f5;
  --line:#d8d8d8;
  --footer:#252525;
  --white:#ffffff;
}
*{margin:0;padding:0;box-sizing:border-box}
html,body{width:891px;height:1200px;overflow:hidden;background:var(--white)}
body{position:relative;font-family:"Roboto",sans-serif;color:var(--ink)}
h1,h2,h3{font-weight:400}
.abs{position:absolute}

/* header */
.brand{left:88px;top:24px;display:flex;align-items:center;gap:8px}
.brand-mark{width:26px;height:26px;background:var(--green)}
.brand-name{font-family:"Raleway",sans-serif;font-weight:700;font-size:20px;color:var(--green);line-height:1}
.brand-sub{font-family:"Raleway",sans-serif;font-size:5px;color:var(--muted);margin-top:3px}
.main-nav{right:100px;top:35px;display:flex;gap:16px;font-family:"Raleway",sans-serif;font-size:13px;color:var(--muted)}
.main-nav .current{color:var(--ink)}

/* hero */
.hero{left:0;top:75px;width:891px;height:277px;background:linear-gradient(180deg,#5a5d5f 0%,#3b3e41 55%,#2f3134 100%)}
.hero-title{left:0;top:125px;width:891px;text-align:center;font-family:"Raleway",sans-serif;font-weight:600;font-size:39px;color:var(--white);letter-spacing:-.5px}
.hero-text{left:0;top:187px;width:891px;text-align:center;font-family:"Raleway",sans-serif;font-weight:400;font-size:15px;line-height:24px;color:var(--white)}
.hero-btn{left:370px;top:281px;width:151px;height:37px;background:var(--green);color:var(--white);font-family:"Raleway",sans-serif;font-weight:700;font-size:16px;display:flex;align-items:center;justify-content:center;border-radius:2px}
.hero-arrow{top:193px}

/* features */
.feature{top:411px;width:130px;text-align:center}
.feature-icon{width:72px;height:72px;border-radius:50%;border:1px solid var(--line);background:#f7f7f7;margin:0 auto;display:flex;align-items:center;justify-content:center}
.feature-icon.active{background:var(--green);border-color:var(--green)}
.feature-label{margin-top:24px;font-size:11px;color:var(--muted);letter-spacing:.2px}
.feature-label.active{color:var(--ink)}

/* welcome band */
.band{left:0;top:582px;width:891px;height:238px;background:var(--soft)}
.welcome-title{left:88px;top:630px;font-family:"Raleway",sans-serif;font-weight:300;font-size:22px;color:var(--ink)}
.welcome-title b{font-weight:600}
.rule{height:1px;background:var(--line)}
.welcome-text{left:88px;top:683px;width:455px;font-size:13px;line-height:20px;color:var(--muted)}
.news{left:574px;top:618px;width:217px;height:182px;background:var(--white);border:1px solid var(--line)}
.news-head{height:38px;background:var(--blue);color:var(--white);font-family:"Raleway",sans-serif;font-size:16.5px;display:flex;align-items:center;padding-left:18px}
.news-head b{font-weight:600;margin-left:4px}
.news-item{position:absolute;left:8px;width:200px;display:flex;gap:11px}
.news-thumb{flex:none;width:43px;height:39px;background:linear-gradient(135deg,#e4b23a,#b5473a 60%,#6a7480)}
.news-title{font-family:"Raleway",sans-serif;font-size:9.5px;color:var(--link)}
.news-body{font-family:"Open Sans",sans-serif;font-size:5.4px;line-height:8.5px;color:var(--muted);margin-top:3px}
.news-body a{color:var(--link);font-weight:600;text-decoration:none}

/* lower columns */
.col-title{top:869px;font-family:"Raleway",sans-serif;font-weight:400;font-size:17px;color:var(--muted)}
.faq{left:92px;width:160px;font-family:"Open Sans",sans-serif;font-size:8.3px;line-height:15px;color:var(--muted);white-space:nowrap}
.faq a{color:var(--link);text-decoration:underline}
.news-sign{left:318px;top:918px;width:200px;font-size:11.5px;line-height:15px;color:var(--muted)}
.news-sign span{color:var(--link)}
.field{left:319px;width:188px;height:25px;border:1px solid var(--green);background:var(--white);font-family:"Open Sans",sans-serif;font-style:italic;font-size:9px;color:var(--muted);padding:6px 9px;display:flex;justify-content:space-between}
.subscribe{left:319px;top:1061px;width:72px;height:24px;background:var(--green);color:var(--white);font-family:"Raleway",sans-serif;font-size:12px;display:flex;align-items:center;justify-content:center;border-radius:2px}
.avatar{width:44px;height:44px;border-radius:50%;border:1px solid var(--line);background:radial-gradient(circle at 50% 40%,#d9c3b0,#5b6068)}
.quote{left:638px;width:120px;font-family:"Lora",serif;font-style:italic;font-weight:400;font-size:7.5px;line-height:11px;color:var(--muted)}
.quote-mark{color:var(--blue);font-size:14px;font-style:normal;font-weight:700;margin-left:-14px;position:absolute}
.quote-by{text-align:right;font-family:"Open Sans",sans-serif;font-style:normal;font-weight:400;font-size:7.5px;color:var(--ink);margin-top:3px}
.quote-by span{color:var(--link)}

/* footer */
.footer{left:0;top:1123px;width:891px;height:77px;background:var(--footer)}
.foot-nav{left:85px;top:1139px;display:flex;gap:16px;font-family:"Raleway",sans-serif;font-size:13px;color:var(--white)}
.copy{left:87px;top:1166px;font-family:"Raleway",sans-serif;font-size:9.5px;color:#d0d0d0}
.social{top:1144px;width:26px;height:26px;border:1.5px solid var(--white);border-radius:50%;display:flex;align-items:center;justify-content:center}
</style>
</head>
<body>

<header>
  <div class="abs brand">
    <div class="brand-mark"></div>
    <div>
      <div class="brand-name">VARNOK</div>
      <div class="brand-sub">Develoipment and Management Corp</div>
    </div>
  </div>
  <nav class="abs main-nav">
    <span class="current">Home</span><span>Services</span><span>Our Team</span><span>Insight Articles</span><span>Contact Us</span>
  </nav>
</header>

<section>
  <div class="abs hero" role="img" aria-label="City skyline of office towers at sunset"></div>
  <h1 class="abs hero-title">SIMPLE. GOOD DESIGN.</h1>
  <p class="abs hero-text">This is sample text only. Lorem ipsum dolor sit amet,<br>consectetur adipisicing elit, sed do eiusmod.</p>
  <div class="abs hero-btn">LEARN MORE</div>
  <svg class="abs hero-arrow" style="left:35px" width="38" height="38" viewBox="0 0 38 38"><circle cx="19" cy="19" r="17.5" fill="rgba(255,255,255,.12)" stroke="#bbb" stroke-width="2"/><path d="M24 10 L12 19 L24 28 L21 19Z" fill="#ccc"/></svg>
  <svg class="abs hero-arrow" style="left:804px" width="38" height="38" viewBox="0 0 38 38"><circle cx="19" cy="19" r="17.5" fill="rgba(255,255,255,.12)" stroke="#bbb" stroke-width="2"/><path d="M14 10 L26 19 L14 28 L17 19Z" fill="#ccc"/></svg>
</section>

<section>
  <div class="abs feature" style="left:128px">
    <div class="feature-icon"><svg width="26" height="22" viewBox="0 0 26 22"><ellipse cx="10" cy="8" rx="8.5" ry="6" fill="none" stroke="#222" stroke-width="2.2"/><path d="M5 13 L3 18 L9 14" fill="#222"/><path d="M18 7 A7.5 5.5 0 0 1 19 18 L23 21 L17 19 A7 5 0 0 1 10 16" fill="none" stroke="#222" stroke-width="2.2"/></svg></div>
    <div class="feature-label">COMMENTS</div>
  </div>
  <div class="abs feature" style="left:284px">
    <div class="feature-icon active"><svg width="24" height="24" viewBox="0 0 24 24"><circle cx="12" cy="13" r="6" fill="#fff"/><path d="M4 13 A8 8 0 0 1 20 13" fill="none" stroke="#fff" stroke-width="2.4"/><rect x="2.5" y="11" width="3.5" height="6" rx="1.5" fill="#fff"/><rect x="18" y="11" width="3.5" height="6" rx="1.5" fill="#fff"/></svg></div>
    <div class="feature-label active">ONLINE SUPPORT</div>
  </div>
  <div class="abs feature" style="left:440px">
    <div class="feature-icon"><svg width="18" height="26" viewBox="0 0 18 26"><path d="M9 25 L2.5 13 A7.5 7.5 0 1 1 15.5 13Z" fill="#222"/><circle cx="9" cy="9" r="3" fill="#f7f7f7"/></svg></div>
    <div class="feature-label">LOCATION</div>
  </div>
  <div class="abs feature" style="left:595px">
    <div class="feature-icon"><svg width="20" height="20" viewBox="0 0 20 20"><rect x="2" y="3" width="13" height="15" fill="none" stroke="#222" stroke-width="1.6"/><path d="M5 8h6M5 11h5M5 14h4" stroke="#222" stroke-width="1.2"/><path d="M11 13 L18 4 L19.5 5.5 L12.5 14.5 L10.5 15Z" fill="#222"/></svg></div>
    <div class="feature-label">CONTACT</div>
  </div>
</section>

<section>
  <div class="abs band"></div>
  <h2 class="abs welcome-title">Welcome to <b>Varnok</b></h2>
  <div class="abs rule" style="left:88px;top:665px;width:67px"></div>
  <p class="abs welcome-text">Culpa qui officia deserunt mollit anim id est laborum. Sed ut perspiciatis unde omnis iste natus error sit voluptatem accusantium doloremque laudantium, totam rem aperiam, eaque ipsa quae ab illo inventore veritatis et quasi archi tecto beatae vitae dicta sunt explicabo.</p>
  <aside class="abs news">
    <div class="news-head">Latest <b>News &amp; Events</b></div>
    <div class="news-item" style="top:50px">
      <div class="news-thumb" role="img" aria-label="Hot air balloon photo"></div>
      <div><div class="news-title">Lorem ipsum doloreum</div><div class="news-body">Lorem ipsum dolor sit amet, consectetur<br>adipisicing elit, sed do eiusmod tempor<br>incididunt ut labore et dol... <a>[Read More]</a></div></div>
    </div>
    <div class="abs rule" style="left:8px;top:106px;width:194px"></div>
    <div class="news-item" style="top:118px">
      <div class="news-thumb" role="img" aria-label="Hot air balloon photo"></div>
      <div><div class="news-title">Lorem ipsum doloreum</div><div class="news-body">Lorem ipsum dolor sit amet, consectetur<br>adipisicing elit, sed do eiusmod tempor<br>incididunt ut labore et dol... <a>[Read More]</a></div></div>
    </div>
  </aside>
</section>

<section>
  <h3 class="abs col-title" style="left:89px">FAQ</h3>
  <div class="abs rule" style="left:89px;top:897px;width:25px"></div>
  <p class="abs faq" style="top:914px">Lorem ipsum dolor sit amet,<br>consectetur adipisicing elit, sed do<br>eiusmod tempor incididunt ut labore<br>et dolore magna aliqua. Ut enim ad<br>minim veniam, quis.. <a>Read More</a></p>
  <div class="abs rule" style="left:88px;top:1006px;width:150px"></div>
  <p class="abs faq" style="top:1016px">Lorem ipsum dolor sit amet,<br>consectetur adipisicing elit, sed do<br>eiusmod tempor incididunt ut labore<br>et dolore magna aliqua. Ut enim ad<br>minim veniam, quis.. <a>Read More</a></p>
  <div class="abs rule" style="left:88px;top:1100px;width:150px"></div>

  <h3 class="abs col-title" style="left:319px">Newsletter</h3>
  <div class="abs rule" style="left:319px;top:897px;width:25px"></div>
  <p class="abs news-sign">Sign up to our newsletter to receive discounts, news, and updates from <span>Varnok Corporation</span></p>
  <div class="abs field" style="top:975px">Name<svg width="10" height="10" viewBox="0 0 10 10"><circle cx="5" cy="3" r="2.5" fill="#aaa"/><path d="M0 10 A5 4 0 0 1 10 10Z" fill="#aaa"/></svg></div>
  <div class="abs field" style="top:1010px">Email<svg width="10" height="8" viewBox="0 0 10 8"><rect width="10" height="8" fill="#aaa"/><path d="M0 0 L5 4 L10 0" fill="none" stroke="#fff"/></svg></div>
  <div class="abs subscribe">Subscribe</div>

  <h3 class="abs col-title" style="left:573px">Testimonials</h3>
  <div class="abs rule" style="left:573px;top:897px;width:25px"></div>
  <svg class="abs" style="left:756px;top:873px" width="36" height="16" viewBox="0 0 36 16"><circle cx="8" cy="8" r="7.5" fill="#aaa"/><path d="M10 4 L6 8 L10 12" fill="none" stroke="#fff" stroke-width="2"/><circle cx="27" cy="8" r="7.5" fill="#aaa"/><path d="M25 4 L29 8 L25 12" fill="none" stroke="#fff" stroke-width="2"/></svg>
  <div class="abs avatar" style="left:575px;top:919px" role="img" aria-label="Portrait of John Doe"></div>
  <div class="abs quote" style="top:922px"><span class="quote-mark">&ldquo;</span>Lorem ipsum dolor sit amet, consectetur adipisicing elit, sed do eiusmod tempor incididunt ut.<div class="quote-by"><span>John Doe</span>, New York</div></div>
  <div class="abs rule" style="left:573px;top:982px;width:186px"></div>
  <div class="abs avatar" style="left:575px;top:1008px" role="img" aria-label="Portrait of Jenna Doe"></div>
  <div class="abs quote" style="top:1011px"><span class="quote-mark">&ldquo;</span>Lorem ipsum dolor sit amet, consectetur adipisicing elit, sed do eiusmod tempor incididunt ut.<div class="quote-by"><span>Jenna Doe</span>, New York</div></div>
  <div class="abs rule" style="left:573px;top:1071px;width:186px"></div>
</section>

<footer>
  <div class="abs footer"></div>
  <nav class="abs foot-nav"><span>Home</span><span>Services</span><span>Our Team</span><span>Insight Articles</span><span>Contact Us</span></nav>
  <p class="abs copy">Copyright&copy;2014Varnok. All Rights Reserved</p>
  <div class="abs social" style="left:651px" aria-label="Email link"><svg width="13" height="10" viewBox="0 0 13 10"><rect x=".5" y=".5" width="12" height="9" fill="none" stroke="#fff" stroke-width="1.2"/><path d="M.5 .5 L6.5 5.5 L12.5 .5" fill="none" stroke="#fff" stroke-width="1.2"/></svg></div>
  <div class="abs social" style="left:689px" aria-label="Chat link"><svg width="13" height="12" viewBox="0 0 13 12"><path d="M1 1h11v7H6L3 11V8H1Z" fill="#fff"/></svg></div>
  <div class="abs social" style="left:727px" aria-label="Share link"><svg width="12" height="12" viewBox="0 0 12 12"><circle cx="9.5" cy="2.5" r="2" fill="#fff"/><circle cx="2.5" cy="6" r="2" fill="#fff"/><circle cx="9.5" cy="9.5" r="2" fill="#fff"/><path d="M9.5 2.5 L2.5 6 L9.5 9.5" fill="none" stroke="#fff" stroke-width="1.2"/></svg></div>
  <div class="abs social" style="left:765px" aria-label="Feed link"><svg width="12" height="12" viewBox="0 0 12 12"><circle cx="2" cy="10" r="1.6" fill="#fff"/><path d="M1 5.5 A5.5 5.5 0 0 1 6.5 11" fill="none" stroke="#fff" stroke-width="1.6"/><path d="M1 1.5 A9.5 9.5 0 0 1 10.5 11" fill="none" stroke="#fff" stroke-width="1.6"/></svg></div>
</footer>

</body>
</html>
```